Design my site www.briefmarkpost.com

So here is what I am thinking in terms of design:

https://plenvo.com

https://www.skylarkjetways.com

http://quillweekly.com/harbor-tower-plaza/

I want the theme to be white and blue (royal blue). I attached a paint picture of what I would like the site to look like in terms of placing the text. Generally, what I like about the sites above is that they are simple, you can navigate easily and have some kind of idea of what's going on by looking at the center (picture and motto). Let's establish a clear understanding of how the functional part of the site would look like. Please see the picture attached.

I want to keep it simple: On top would be the Name 'BRIEFMARK post", somewhere to the right on top on the page would be 'Sign in" button.

In the center would be a picture (maybe a video) with the Motto (on top of it all in capital) OBSERVE NAVIGATE DECIDE and below would be the "sign up now"

Below the picture (like on quillweekly.com site) or to the left on top of the page would be "About Us', "Press" "Contact Us' buttons.

Then once the user gets to his page his got 3 tabs " Press Headlines", "Events", " Briefings".

we would keep the same format I only have on the site, but separate for every Tab.

I do not want the user to get distracted. I also want him to be able to access the page though mobile phone and be able to get automatic updates just like Zentro Pings without having to sign in daily.

The landing page must be minimalist yet with business/corporate feel where users can navigate easily and a "what you see is what you get" approach. You want an image or video (personally I prefer the video.. it does capture the users attention instantly, as long as it is an interesting video), with your taglines in it.

Sections available to public: About Us, Contact Us, Landing Page with Signup Option

Private: Public Sections + User Account Page, Tabs for (Events, Press Headlines, Briefings)

Target Market(s)

PR/media monitoring/diplomatic community

Coding

Coded - Design and coding required

Number of Pages Required

1 page

Font styles to use
Serif
Sans Serif

Colors
0255a3
ec1f27

Requirements
Must have
• a simple landing page, that is user friendly.
Nice to have
• a video with the explanation of how to navigate the site
Should not have
• too many colors, graphs etc.

```html
<!DOCTYPE html>
<html lang="en">
<head>
<meta charset="utf-8">
<title>BRIEFMARK post — Headlines</title>
<link rel="stylesheet" href="https://fonts.googleapis.com/css2?family=Jost:wght@500;600&family=Open+Sans:wght@400;600;700&display=swap">
<style>
  :root {
    --royal: #0255a3;
    --royal-bright: #3d8ee6;
    --royal-deep: #02305e;
    --navy: #041a33;
    --white: #ffffff;
    --tab-idle: rgba(255, 255, 255, 0.16);
    --tab-idle-border: rgba(255, 255, 255, 0.35);
    --tab-shadow: rgba(1, 20, 45, 0.6);
    --thumb-light: #9fc3ec;
    --thumb-mid: #3f77b8;
  }
  * { box-sizing: border-box; margin: 0; padding: 0; }
  html, body { width: 1200px; height: 600px; overflow: hidden; }
  body {
    position: relative;
    font-family: "Open Sans", Arial, sans-serif;
    color: var(--white);
    background: var(--navy);
  }
  .city-backdrop {
    position: absolute; inset: 0;
    background:
      radial-gradient(ellipse at 55% 30%, rgba(61, 142, 230, 0.35), transparent 60%),
      linear-gradient(180deg, var(--navy) 0%, var(--royal-deep) 45%, #0a3f78 75%, var(--navy) 100%);
  }
  .city-backdrop::after {
    content: ""; position: absolute; inset: 0;
    background: rgba(2, 16, 36, 0.25);
  }
  .brand {
    position: absolute; left: 160px; top: 22px;
    font-weight: 700; font-size: 17px; letter-spacing: 0.5px;
    color: var(--white);
    display: flex; align-items: center; gap: 8px;
  }
  .brand-square { width: 10px; height: 10px; background: var(--white); }
  .signup-button {
    position: absolute; left: 956px; top: 12px;
    width: 82px; height: 29px;
    border: 1.5px solid var(--white); border-radius: 15px;
    font-weight: 700; font-size: 10.5px; letter-spacing: 0.4px;
    display: flex; align-items: center; justify-content: center;
    color: var(--white); text-decoration: none;
  }
  .tabs { position: absolute; top: 114px; left: 188px; height: 69px; }
  .tab {
    position: absolute; top: 0; height: 69px;
    display: flex; align-items: center; justify-content: center;
    font-family: "Jost", "Futura", sans-serif; font-weight: 600;
    font-size: 20px; letter-spacing: 0.2px; text-transform: uppercase;
    background: var(--tab-idle);
    border: 1px solid var(--tab-idle-border);
    border-radius: 2px;
    box-shadow: 0 3px 0 var(--tab-shadow);
  }
  .tab--active { background: var(--royal); border-color: var(--royal); }
  .tab--active::after {
    content: ""; position: absolute; left: 50%; bottom: -10px;
    transform: translateX(-50%);
    border-left: 9px solid transparent; border-right: 9px solid transparent;
    border-top: 9px solid var(--royal);
  }
  .tab-headlines { left: 0; width: 338px; }
  .tab-events { left: 341px; width: 204px; }
  .tab-briefing { left: 548px; width: 277px; }
  .story-grid {
    position: absolute; left: 214px; top: 230px;
    display: grid; grid-template-columns: 420px 420px;
    grid-template-rows: 193px 193px;
  }
  .story { display: flex; gap: 17px; }
  .story-thumb {
    width: 98px; height: 90px; border-radius: 3px; flex: none;
    background: linear-gradient(135deg, var(--thumb-light), var(--thumb-mid) 55%, #cfe0f5);
  }
  .story-meta { display: flex; align-items: center; font-size: 12px; margin-left: 2px; }
  .story-date { position: relative; padding-right: 11px; border-right: 1.5px solid var(--white); line-height: 16px; }
  .story-date::after {
    content: ""; position: absolute; left: 0; bottom: -8px;
    width: 36px; height: 1px; background: var(--white);
  }
  .story-place { padding-left: 11px; }
  .story-title { margin-top: 14px; font-size: 16px; line-height: 18px; font-weight: 400; width: 260px; }
  .read-more {
    display: inline-block; margin-top: 14px; font-size: 12px;
    color: var(--white); text-decoration: none;
    padding-bottom: 4px; border-bottom: 2px solid var(--royal-bright);
    padding-right: 1px;
  }
</style>
</head>
<body>
  <div class="city-backdrop" role="img" aria-label="Aerial photo of a city skyline with a tall spire at dusk"></div>

  <div class="brand"><span class="brand-square"></span>BRIEFMARK post</div>
  <a class="signup-button" href="#">SIGN UP</a>

  <nav class="tabs">
    <div class="tab tab-headlines tab--active">Newspapers Headlines</div>
    <div class="tab tab-events">Events</div>
    <div class="tab tab-briefing">Daily Briefing</div>
  </nav>

  <main class="story-grid">
    <article class="story">
      <div class="story-thumb" role="img" aria-label="Overhead photo of a busy city street with taxis"></div>
      <div>
        <div class="story-meta"><span class="story-date">Jan 05, 2016</span><span class="story-place">New York</span></div>
        <h2 class="story-title">Duis autem vel eum iriure dolor in hendrerit in vulputate velit molest ievel illum</h2>
        <a class="read-more" href="#">Read More</a>
      </div>
    </article>
    <article class="story">
      <div class="story-thumb" role="img" aria-label="Overhead photo of a busy city street with taxis"></div>
      <div>
        <div class="story-meta"><span class="story-date">Jan 05, 2016</span><span class="story-place">New York</span></div>
        <h2 class="story-title">Duis autem vel eum iriure dolor in hendrerit in vulputate velit molest ievel illum</h2>
        <a class="read-more" href="#">Read More</a>
      </div>
    </article>
    <article class="story">
      <div class="story-thumb" role="img" aria-label="Overhead photo of a busy city street with taxis"></div>
      <div>
        <div class="story-meta"><span class="story-date">Jan 05, 2016</span><span class="story-place">New York</span></div>
        <h2 class="story-title">Duis autem vel eum iriure dolor in hendrerit in vulputate velit molest ievel illum</h2>
        <a class="read-more" href="#">Read More</a>
      </div>
    </article>
    <article class="story">
      <div class="story-thumb" role="img" aria-label="Overhead photo of a busy city street with taxis"></div>
      <div>
        <div class="story-meta"><span class="story-date">Jan 05, 2016</span><span class="story-place">New York</span></div>
        <h2 class="story-title">Duis autem vel eum iriure dolor in hendrerit in vulputate velit molest ievel illum</h2>
        <a class="read-more" href="#">Read More</a>
      </div>
    </article>
  </main>
</body>
</html>
```